Business Card design project for new family-run construction business

We need a logo and business card designed for a new construction company. We want to convey a professional, but approachable image. We hope to be servicing small residential clients as well as large commercial contracts as well.
Our business will employ a single "Hydro excavator" truck, which can be used for multiple purposes: vacuuming up dirt or water, digging holes, clearing sewer blockages and so on.
We are open to different colour schemes, however blue and white, or yellow/green would be good combinations. We are open to multiple colours (2-4), so long as they are complimentary.

EDIT: Let's not put much emphasis on the octopus... unless it's very clear that the arms are actual vacuum hoses, it won't make sense. An octopus on it's own has little to do with our business.

Please also do not use actual photos of hydro-vac trucks. This is not the aesthetic we are going for.

**The logo should instead be: A stylized outline of a hydrovac truck (a line drawing or digital version of a line-drawing). See the two examples in the attached images of hydrovac trucks. I've also included a very crude pen outline as a reference. Please use your artistic discretion and talent (as I clearly have none) to make something that looks much nicer. Thanks for your efforts!**

The front of the card should have the following elements:
Logo
Name: P & K Hydro Excavation and Flushign
Two phone numbers: Direct and Office
Email address
Website
It should also have the name of the employee and their job title
At the bottom of the card it should say (in a noticeable way): "24/7 Emergency Calls Welcome"

The back of the card should have the following elements:
"20 Years Experience"
"A Canadian Family Run Business"
A small maple-leaf logo that is in a similar style to the rest of the card/logos in the bottom right corner of the back of the card. (see attached)

**We have just added a number of business card designs that really appeal to us to offer inspiration.**

Reason: We have not received designs that hit the mark of what we are looking for. Feedback has been posted, so we would like to provide the designers more time.

Target Market(s)

Commercial and residential customers. As big as large malls and office buildings, as small single-family home owners

Industry/Entity Type

Construction Company

Contact Information for Business Card

We have just added a number of business card designs that really appeal to us to offer inspiration.

Logo
Email address
Website

"20 Years Experience"

Logo Text

P & K Hydro Excavation and Flushing

Font styles to use
Serif
Sans Serif
Other font styles liked:
• Helvetica, Futura, Impact, bold strong, modern fonts that convey a sense of design and style

Colors
0592cd
ec1f27
9bcb3c

Requirements
Must have
• The front of the card should have the following elements:
• Logo
• Name: P & K Hydro Excavation and Flushign
• Two phone numbers: Direct and Office
• Email address
• Website
• It should also have the name of the employee and their job title
• At the bottom of the card it should say (in a noticeable way): "24/7 Emergency Calls Welcome"
• The back of the card should have the following elements:
• "20 Years Experience"
• "A Canadian Family Run Business"
• A small maple-leaf logo that is in a similar style to the rest of the card/logos in the bottom right corner of the back of the card. (see attached)
Nice to have
• The card does not have to be a perfect rectangle. We are open to rounded corners or cut out elements.
• Also embossing, engraving, adding highlighted/glossy layers (spot glass?), or any other effect that will give the card a unique look/feel is more than welcome.
• We would love to have a card that stands out from others and is compelling to look at it, so we are happy to incorporate any sort of modern printing technology to bring out the design.
• Please feel encouraged to be creative and design something unique, especially for this industry.
• Our dream would be if a Scandinavian architect were to go into the construction business and design this business card ;)
Should not have
• Photographs

```html
<!DOCTYPE html>
<html lang="en">
<head>
<meta charset="utf-8">
<title>P &amp; K Hydro Excavation and Flushing – Business Card</title>
<link rel="stylesheet" href="https://fonts.googleapis.com/css2?family=Poppins:wght@300;400;500;600;700&family=Lora:wght@400&display=swap">
<style>
  :root {
    --page: #eceeef;
    --night: #1c2230;
    --coal: #1e1f22;
    --sky: #4cc3f5;
    --azure: #2f8fe0;
    --white: #ffffff;
    --muted: #b9bcc2;
    --leaf: #d8232a;
  }
  * { margin: 0; padding: 0; box-sizing: border-box; }
  html, body {
    width: 1200px; height: 1200px; overflow: hidden;
    background: var(--page);
    font-family: "Poppins", Arial, sans-serif;
  }
  .sheet {
    position: relative; width: 1200px; height: 1200px;
    display: flex; flex-direction: column; align-items: center; justify-content: center;
    gap: 48px;
  }
  .card {
    position: relative; width: 900px; height: 514px; overflow: hidden;
    background: var(--night);
    box-shadow: 0 6px 18px rgba(0,0,0,0.18);
  }
  .card__art { position: absolute; inset: 0; width: 100%; height: 100%; }
  .card__text { position: absolute; color: var(--white); white-space: nowrap; }

  /* Back */
  .back__headline {
    left: 200px; top: 180px;
    font-size: 44px; font-weight: 600; letter-spacing: 1px;
  }
  .back__tagline {
    left: 250px; top: 244px;
    font-family: "Lora", Georgia, serif; font-size: 24px;
  }
  .back__leaf {
    position: absolute; left: 806px; top: 170px;
    width: 26px; height: 26px; background: var(--leaf);
  }

  /* Front */
  .front__rule { position: absolute; height: 3px; background: var(--white); }
  .front__brand-mark {
    position: absolute; left: 48px; top: 128px;
    width: 62px; height: 62px; border-radius: 50%;
    background: var(--sky);
  }
  .front__brand-name {
    left: 128px; top: 106px;
    font-size: 44px; font-weight: 700; letter-spacing: 2px;
  }
  .front__brand-line {
    left: 128px; top: 160px;
    font-size: 26px; font-weight: 300;
  }
  .front__person {
    left: 60px; top: 336px;
    font-size: 38px; font-weight: 300; letter-spacing: 0.5px;
  }
  .front__person strong { font-weight: 700; }
  .front__role {
    left: 62px; top: 392px;
    font-size: 21px; font-weight: 300; color: var(--muted);
  }
  .contact {
    position: absolute; left: 640px;
    display: flex; align-items: center; gap: 14px;
  }
  .contact--phone { top: 322px; }
  .contact--web { top: 386px; }
  .contact__icon { width: 36px; height: 36px; flex: none; }
  .contact__lines { color: var(--white); font-size: 15px; line-height: 1.3; }
  .front__emergency {
    left: 0; right: 0; bottom: 8px; text-align: center; padding-left: 260px;
    font-size: 21px; font-weight: 500; letter-spacing: 1px;
  }
</style>
</head>
<body>
<main class="sheet">

  <section class="card card--back" aria-label="Card back">
    <svg class="card__art" viewBox="0 0 900 514" preserveAspectRatio="none">
      <defs>
        <linearGradient id="truck-photo-back" x1="0" y1="0" x2="1" y2="1">
          <stop offset="0" stop-color="#1a2130"/>
          <stop offset="0.55" stop-color="#2b3344"/>
          <stop offset="1" stop-color="#1a2030"/>
        </linearGradient>
      </defs>
      <rect width="900" height="514" fill="url(#truck-photo-back)" role="img" aria-label="Darkened photo of a hydro-vac truck"/>
      <polygon points="0,514 0,455 560,360 900,232 900,252 300,514" fill="var(--sky)"/>
      <polygon points="430,430 900,240 900,252 360,490" fill="var(--azure)"/>
      <polygon points="300,514 900,252 900,514" fill="var(--coal)"/>
    </svg>
    <p class="card__text back__headline">20 YEARS EXPERIENCE</p>
    <p class="card__text back__tagline">A Canadian Family Run Business</p>
    <div class="back__leaf"></div>
  </section>

  <section class="card card--front" aria-label="Card front">
    <svg class="card__art" viewBox="0 0 900 514" preserveAspectRatio="none">
      <defs>
        <linearGradient id="truck-photo-front" x1="0" y1="0" x2="1" y2="1">
          <stop offset="0" stop-color="#1a2130"/>
          <stop offset="0.5" stop-color="#2a3242"/>
          <stop offset="1" stop-color="#1a2030"/>
        </linearGradient>
      </defs>
      <rect width="900" height="514" fill="url(#truck-photo-front)" role="img" aria-label="Darkened photo of hydro-vac trucks"/>
      <polygon points="650,0 900,0 900,110 560,300" fill="var(--sky)"/>
      <polygon points="900,110 900,135 330,470 560,300" fill="var(--azure)"/>
      <polygon points="330,470 900,135 900,470" fill="var(--coal)"/>
      <rect x="0" y="470" width="900" height="44" fill="var(--sky)"/>
      <polygon points="0,470 330,470 0,500" fill="var(--azure)"/>
    </svg>

    <div class="front__rule" style="left:128px; top:96px; width:380px;"></div>
    <div class="front__brand-mark"></div>
    <p class="card__text front__brand-name">P &amp; K</p>
    <p class="card__text front__brand-line">Hydro Excavation and Flushign</p>

    <div class="front__rule" style="left:60px; top:324px; width:400px;"></div>
    <p class="card__text front__person"><strong>FIRST</strong> LASTNAME</p>
    <p class="card__text front__role">Job Title</p>

    <div class="contact contact--phone">
      <svg class="contact__icon" viewBox="0 0 36 36" aria-hidden="true">
        <circle cx="18" cy="18" r="18" fill="var(--sky)"/>
        <path d="M12 10c1-1 2-1 3 0l2 3c.6 1 .3 1.7-.5 2.4l-1 .8c.8 2 2.3 3.6 4.3 4.4l.8-1c.7-.8 1.5-1.1 2.4-.5l3 2c1 .7 1 2 0 3l-1.3 1.3c-1 1-2.6 1.2-4 .5-4.3-2-7.6-5.3-9.6-9.6-.7-1.4-.5-3 .5-4z" fill="var(--white)"/>
      </svg>
      <p class="contact__lines">123-456-7890 (Direct)<br>987-654-3210 (Office)</p>
    </div>

    <div class="contact contact--web">
      <svg class="contact__icon" viewBox="0 0 36 36" aria-hidden="true">
        <circle cx="18" cy="18" r="18" fill="var(--sky)"/>
        <g fill="none" stroke="var(--white)" stroke-width="1.6">
          <circle cx="18" cy="18" r="9"/>
          <ellipse cx="18" cy="18" rx="4" ry="9"/>
          <line x1="9" y1="18" x2="27" y2="18"/>
          <line x1="10.5" y1="13.5" x2="25.5" y2="13.5"/>
          <line x1="10.5" y1="22.5" x2="25.5" y2="22.5"/>
        </g>
      </svg>
      <p class="contact__lines">name@website.com<br>www.website.com</p>
    </div>

    <p class="card__text front__emergency">24/7 Emergency Calls Welcome</p>
  </section>

</main>
</body>
</html>
```